Tidal Brookfield ( New Product Range Office Furniture )

We are looking a dedicated page within our website www.quarnex.com.au ( must be Magento compatible ) to launch our new brand " TIDAL Brookfield "

We have our existing Brand "KEMO" has been selling in the last 10 years in Australia, We have just manufactured our new range please go our website and type "Tidal" in the search box.

The ideal is to have this page to showcase our new products in more professional manner, target audience is corporate customers.

We are also working with a office designers who they will use our website to show their clients with our products

Key Note
This web page is an additional page to be added to our existing website,

so WE DO NOT NEED SHOPPING CART in these pages,

Which means, when customer click on these pages, they will see a total corporate presentation of our Tidal Brookfield.

What we want to see is below

We want to showcase each product individually with main image with Long Description, because our product is a modular system we want to add thumbnail images to show 4 more different type of combination images (images to be provided later) so total of 5 images (we can live with 4 images if better spacing when design)

we need a good background theme to make sure they are all match nicely

Hope the above notes will help you get us a better design

Target Market(s)

Corporate End Users, Also Office Interior Designers

Industry/Entity Type

Office Furniture

Number of Pages Required

2 page

Font styles to use
Sans Serif

Requirements
Must have
• Our Tidal Brookfield product images ( can get from our website for now )
Nice to have
• Our Product Tidal Brookfield Range is a modular system, there are so many configuration that our customer can use to setup their office

```html
<!DOCTYPE html>
<html lang="en">
<head>
<meta charset="utf-8">
<title>Tidal Brookfield 1800 Open Hutch</title>
<link rel="stylesheet" href="https://fonts.googleapis.com/css2?family=Open+Sans:wght@400;600;700&display=swap">
<style>
  :root {
    --page-bg: #3b3b3b;
    --overlay: rgba(28, 28, 28, 0.72);
    --modal-bg: #f4f4f4;
    --frame: #d4d4d4;
    --ink: #1b1b1b;
    --body-ink: #4a4a4a;
    --muted: #5d5d5d;
    --rule: #dcdcdc;
    --accent: #0a7fd3;
    --tick: #1a7fc8;
    --icon-bg: #cfcfcf;
    --brand-blue: #1e5a9c;
  }
  * { box-sizing: border-box; margin: 0; padding: 0; }
  html, body { width: 1200px; height: 658px; overflow: hidden; }
  body {
    position: relative;
    background: var(--page-bg);
    font-family: "Open Sans", Arial, sans-serif;
  }

  /* Underlying page */
  .page { position: absolute; inset: 0; }
  .brand { position: absolute; left: 85px; top: 4px; display: flex; align-items: center; gap: 10px; }
  .brand-mark { width: 32px; height: 32px; background: var(--brand-blue); }
  .brand-name { font-size: 24px; font-weight: 700; color: var(--brand-blue); letter-spacing: 1px; }
  .hours { position: absolute; left: 650px; top: 2px; font-size: 10px; color: #8a8a8a; line-height: 16px; }
  .search { position: absolute; left: 874px; top: -6px; width: 240px; height: 20px; font-size: 10px; color: #8a8a8a; }
  .account { position: absolute; left: 953px; top: 28px; font-size: 10px; color: #8a8a8a; letter-spacing: .5px; }
  .nav { position: absolute; left: 85px; top: 84px; font-size: 11px; color: #8a8a8a; word-spacing: 18px; }
  .card { position: absolute; background: #d8d8d8; }
  .card-left { left: 101px; top: 150px; width: 70px; height: 340px; }
  .card-right { left: 1030px; top: 145px; width: 82px; height: 345px; }
  .card-label { position: absolute; font-size: 12px; font-weight: 600; color: #555; letter-spacing: 1px; line-height: 21px; }
  .latest { position: absolute; left: 85px; top: 550px; font-size: 19px; font-weight: 700; color: #222; }
  .latest span { color: var(--brand-blue); }
  .latest-sub { position: absolute; left: 85px; top: 590px; font-size: 12px; color: #666; }
  .overlay { position: absolute; inset: 0; background: var(--overlay); }

  /* Quick view modal */
  .quickview {
    position: absolute; left: 147px; top: 66px; width: 905px; height: 465px;
    background: var(--modal-bg);
    box-shadow: 0 4px 14px rgba(0,0,0,.5);
  }
  .gallery-main {
    position: absolute; left: 26px; top: 26px; width: 414px; height: 335px;
    border: 1px solid var(--frame);
    background: linear-gradient(160deg, #ffffff 0%, #ededed 55%, #cfcfcf 100%);
  }
  .thumbs { position: absolute; left: 26px; top: 371px; display: flex; gap: 18px; }
  .thumb {
    position: relative; width: 90px; height: 72px;
    border: 1px solid var(--frame);
    background: linear-gradient(160deg, #ffffff 0%, #e3e3e3 60%, #bdbdbd 100%);
  }
  .thumb.is-active::after {
    content: ""; position: absolute; inset: 0; background: rgba(90,90,90,.75);
  }
  .thumb-zoom { position: absolute; left: 36px; top: 27px; z-index: 1; }

  .details { position: absolute; left: 466px; top: 30px; width: 414px; }
  .product-title {
    font-size: 17.5px; font-weight: 700; color: var(--ink); letter-spacing: .2px;
    padding-bottom: 8px; border-bottom: 1px solid var(--rule);
  }
  .product-desc { margin-top: 17px; font-size: 11px; line-height: 21px; color: var(--body-ink); letter-spacing: -0.15px; }
  .features { list-style: none; margin-top: 13px; }
  .features li { position: relative; padding-left: 25px; font-size: 11px; line-height: 21px; color: var(--body-ink); }
  .features svg { position: absolute; left: 1px; top: 6px; }

  .actions { display: flex; gap: 22px; position: absolute; left: 466px; top: 343px; }
  .action { display: flex; align-items: center; gap: 11px; font-size: 12px; color: var(--muted); letter-spacing: .8px; }
  .action-icon {
    width: 32px; height: 32px; border-radius: 50%; background: var(--icon-bg);
    display: flex; align-items: center; justify-content: center;
  }
  .view-details {
    position: absolute; left: 731px; top: 392px; width: 147px; height: 34px;
    background: var(--accent); color: #fff; font-size: 11.5px; font-weight: 400;
    display: flex; align-items: center; justify-content: center; letter-spacing: .2px;
  }
</style>
</head>
<body>
  <div class="page">
    <div class="brand"><span class="brand-mark"></span><span class="brand-name">QUARNEX</span></div>
    <div class="hours">Saturday: 8AM - 2PM<br>Sundays &amp; Public Holidays : Closed</div>
    <div class="search">Search</div>
    <div class="account">♥ MY WISHLIST &nbsp;&nbsp;&nbsp; MY CART (0)</div>
    <div class="nav">Desking Seating Storage Workstations Reception</div>
    <div class="card card-left"></div>
    <div class="card card-right"></div>
    <div class="card-label" style="left:97px; top:440px;">TIDAL<br>FILING</div>
    <div class="card-label" style="left:1050px; top:285px;">RWOOD<br>DENZA</div>
    <div class="latest"><span>LATEST</span> PRODUCTS</div>
    <div class="latest-sub">Voluptatem accusantium doloremque laudantium, totam rem aperiam</div>
  </div>
  <div class="overlay"></div>

  <section class="quickview">
    <div class="gallery-main" role="img" aria-label="Product photo: Tidal Brookfield 1800 open hutch in charcoal with light timber shelves, marked new colour"></div>

    <div class="thumbs">
      <div class="thumb is-active" role="img" aria-label="Hutch configuration thumbnail 1">
        <svg class="thumb-zoom" width="18" height="18" viewBox="0 0 18 18" aria-hidden="true">
          <circle cx="7.5" cy="7.5" r="5.5" fill="none" stroke="#fff" stroke-width="2.2"/>
          <line x1="11.5" y1="11.5" x2="16" y2="16" stroke="#fff" stroke-width="2.6" stroke-linecap="round"/>
        </svg>
      </div>
      <div class="thumb" role="img" aria-label="Hutch configuration thumbnail 2"></div>
      <div class="thumb" role="img" aria-label="Hutch configuration thumbnail 3"></div>
      <div class="thumb" role="img" aria-label="Hutch configuration thumbnail 4"></div>
    </div>

    <div class="details">
      <h1 class="product-title">TIDAL BROOKFIELD 1800 OPEN HUTCH</h1>
      <p class="product-desc">The Tidal 1800 Hutch combines impressive storage space with the elegant style and premium quality melamine construction. With its six compartments and huge tabletop surface it will provide more than enough space to keep all of your documents, books, accessories and more. This office hutch features an adjustable shelf which can be moved if needed and it has a 10 year warranty.</p>
      <ul class="features">
        <li><svg width="11" height="9" viewBox="0 0 11 9"><path d="M1 4.5 L4 7.5 L10 1" fill="none" stroke="var(--tick)" stroke-width="2.2"/></svg>Soft Textured Melamine Surface</li>
        <li><svg width="11" height="9" viewBox="0 0 11 9"><path d="M1 4.5 L4 7.5 L10 1" fill="none" stroke="var(--tick)" stroke-width="2.2"/></svg>E1 Melamine Board (Australian Standard)</li>
        <li><svg width="11" height="9" viewBox="0 0 11 9"><path d="M1 4.5 L4 7.5 L10 1" fill="none" stroke="var(--tick)" stroke-width="2.2"/></svg>Features 25mm tops and ABS edging</li>
        <li><svg width="11" height="9" viewBox="0 0 11 9"><path d="M1 4.5 L4 7.5 L10 1" fill="none" stroke="var(--tick)" stroke-width="2.2"/></svg>Dimensions: 1800L x 315W x 1050H mm</li>
        <li><svg width="11" height="9" viewBox="0 0 11 9"><path d="M1 4.5 L4 7.5 L10 1" fill="none" stroke="var(--tick)" stroke-width="2.2"/></svg>Adjustable Shelves</li>
        <li><svg width="11" height="9" viewBox="0 0 11 9"><path d="M1 4.5 L4 7.5 L10 1" fill="none" stroke="var(--tick)" stroke-width="2.2"/></svg>Comes with a 10 Year Warranty</li>
      </ul>
    </div>

    <div class="actions">
      <div class="action">
        <span class="action-icon">
          <svg width="14" height="12" viewBox="0 0 14 12" aria-hidden="true"><path d="M7 11.5 L1.6 6.2 A3.1 3.1 0 0 1 7 2.2 A3.1 3.1 0 0 1 12.4 6.2 Z" fill="#555"/></svg>
        </span>ADD TO WISHLIST
      </div>
      <div class="action">
        <span class="action-icon">
          <svg width="14" height="14" viewBox="0 0 14 14" aria-hidden="true"><rect x="1.5" y="4" width="7" height="8.5" fill="none" stroke="#555" stroke-width="1.3"/><rect x="5.5" y="1.5" width="7" height="8.5" fill="#cfcfcf" stroke="#555" stroke-width="1.3"/></svg>
        </span>ADD TO COMPARE
      </div>
    </div>

    <a class="view-details">VIEW DETAILS</a>
  </section>
</body>
</html>
```